Business Card Design

I need a business card for a new company based in Australia called "MedLinkora".

Its a cloud program for GPs that allows them to search for the specialist they require using a simple user friendly tool.

I would like the colours to match those in the program (the colours in the logo attached).

The final design should reflect the programs clarity, ease of use and professionalism.

Target Market(s)

GPs and other Health Professionals

Industry/Entity Type

Business

Contact Information for Business Card

MedLinkora; The Trusted Clinician Index; Marla Ostrove CEO; 0438215906; marla@medlinkora.example; www.medlinkora.example

Requirements
Must have
• Must have the logo attached; the web address and my name and phone number
Nice to have
• the slogan "The Trusted Clinician Index"

```html
<!DOCTYPE html>
<html lang="en">
<head>
<meta charset="utf-8">
<title>MedLinkora Business Card</title>
<link href="https://fonts.googleapis.com/css2?family=Lato:wght@300;400;700&display=swap" rel="stylesheet">
<style>
  :root {
    --bg: #e6e6e6;
    --card-dark: #333333;
    --card-light: #ffffff;
    --brand-blue: #29abe2;
    --tag-grey: #8a8a8a;
    --tag-grey-dark: #9a9a9a;
    --ink: #2b2b2b;
    --tab-dark: #3a3a3a;
  }
  * { margin: 0; padding: 0; box-sizing: border-box; }
  html, body {
    width: 1200px; height: 1000px; overflow: hidden;
    background: var(--bg);
    font-family: "Lato", sans-serif;
  }
  .stage { position: relative; width: 1200px; height: 1000px; }
  .card {
    position: absolute; left: 250px; width: 700px; height: 400px;
    border-radius: 4px;
    box-shadow: 0 6px 18px rgba(0,0,0,0.18);
    overflow: hidden;
  }
  /* Back side */
  .card--back { top: 60px; background: var(--card-dark); }
  .card--back .wordmark {
    position: absolute; left: 0; right: 0; top: 130px;
    text-align: center;
  }
  .card--back .wordmark__name {
    font-weight: 400; font-size: 84px; letter-spacing: -1px;
    color: var(--brand-blue); line-height: 1;
  }
  .card--back .wordmark__tagline {
    margin-top: 10px;
    font-weight: 300; font-size: 30px; color: var(--tag-grey-dark);
    letter-spacing: 0.5px;
  }
  /* Front side */
  .card--front { top: 540px; background: var(--card-light); }
  .name-bar {
    position: absolute; left: 0; top: 44px; width: 330px; height: 40px;
    background: var(--brand-blue);
    border-radius: 0 6px 6px 0;
    padding-left: 64px;
    display: flex; align-items: center;
    color: #fff; font-weight: 700; font-size: 27px;
  }
  .role {
    position: absolute; left: 64px; top: 92px;
    font-size: 20px; color: var(--ink);
  }
  .contact-tab {
    position: absolute; left: 0; top: 238px; width: 36px; height: 112px;
    background: var(--tab-dark);
    border-radius: 0 6px 6px 0;
    display: flex; flex-direction: column; justify-content: space-around;
    align-items: center; padding: 8px 0;
  }
  .contact-tab svg { width: 19px; height: 19px; fill: #ffffff; }
  .contact-list {
    position: absolute; left: 52px; top: 244px;
    list-style: none;
  }
  .contact-list li {
    font-size: 20px; color: var(--ink); line-height: 34px;
    letter-spacing: 0.2px;
  }
  .card--front .wordmark {
    position: absolute; right: 34px; bottom: 30px; text-align: left;
  }
  .card--front .wordmark__name {
    font-weight: 400; font-size: 52px; letter-spacing: -1px;
    color: var(--brand-blue); line-height: 1;
  }
  .card--front .wordmark__tagline {
    margin-top: 6px;
    font-weight: 300; font-size: 17px; color: var(--tag-grey);
    letter-spacing: 0.4px;
  }
</style>
</head>
<body>
<main class="stage">
  <section class="card card--back" aria-label="Card back">
    <div class="wordmark">
      <div class="wordmark__name">MedLinkora</div>
      <div class="wordmark__tagline">The Trusted Clinician Index</div>
    </div>
  </section>

  <section class="card card--front" aria-label="Card front">
    <div class="name-bar">Marla Ostrove</div>
    <div class="role">CEO</div>

    <div class="contact-tab" aria-hidden="true">
      <svg viewBox="0 0 24 24"><path d="M6.6 10.8a15 15 0 0 0 6.6 6.6l2.2-2.2a1 1 0 0 1 1-.25 11.4 11.4 0 0 0 3.6.57 1 1 0 0 1 1 1V20a1 1 0 0 1-1 1A17 17 0 0 1 3 4a1 1 0 0 1 1-1h3.5a1 1 0 0 1 1 1c0 1.25.2 2.45.57 3.57a1 1 0 0 1-.25 1z"/></svg>
      <svg viewBox="0 0 24 24"><path d="M2 5h20v14H2z M3.5 6.5 12 13l8.5-6.5" fill="none" stroke="#fff" stroke-width="1.8"/></svg>
      <svg viewBox="0 0 24 24"><circle cx="12" cy="12" r="9" fill="none" stroke="#fff" stroke-width="1.8"/><path d="M3 12h18M12 3c3 3.2 3 14.8 0 18M12 3c-3 3.2-3 14.8 0 18" fill="none" stroke="#fff" stroke-width="1.5"/></svg>
    </div>
    <ul class="contact-list">
      <li>0438215906</li>
      <li>marla@medlinkora.example</li>
      <li>www.medlinkora.example</li>
    </ul>

    <div class="wordmark">
      <div class="wordmark__name">MedLinkora</div>
      <div class="wordmark__tagline">The Trusted Clinician Index</div>
    </div>
  </section>
</main>
</body>
</html>
```